Dunmore Ag Solutions, LLC

Sales, Service, and Repair of Grain Bins

Must include: Insured

Industry/Entity Type

Sales

Contact Information for Business Card

We would like the submitted file to be used in making the business card. Either shrinking it down to use as a "logo" in the left hand side or use it as a back drop with writing over top of it. Would like to have on card also is a name and number: Todd Dunmore (555) 268-0137

Font styles to use
Serif

Requirements
Must have
• Name of owner: Todd Dunmore phone number: 555 268 0137. Free estimates
Nice to have
• Simple and neat design, needs to have the word insured somewhere on the card

```html
<!DOCTYPE html>
<html lang="en">
<head>
<meta charset="utf-8">
<title>Dunmore Ag Solutions, LLC – Business Card</title>
<link rel="stylesheet" href="https://fonts.googleapis.com/css2?family=Roboto+Slab:wght@700;800&family=Noto+Serif:wght@400&display=swap">
<style>
  :root {
    --tan: #b98c63;
    --stripe: #b5ab93;
    --ink: #000000;
    --paper: #ffffff;
    --bin-area: #ad8159;
    --name-shadow: #d8c3ac;
  }
  html, body {
    margin: 0;
    padding: 0;
    overflow: hidden;
    background: var(--paper);
  }
  .card {
    position: relative;
    width: 1200px;
    height: 686px;
    overflow: hidden;
    background: var(--paper);
  }
  .card-backdrop {
    position: absolute;
    inset: 0;
  }
  .owner-name {
    position: absolute;
    left: 546px;
    top: 146px;
    margin: 0;
    font-family: "Roboto Slab", serif;
    font-weight: 700;
    font-size: 52px;
    line-height: 1;
    letter-spacing: 0;
    color: var(--tan);
    text-shadow: 3px 3px 0 var(--name-shadow);
    white-space: nowrap;
  }
  .phone-bar {
    position: absolute;
    left: 503px;
    top: 222px;
    width: 497px;
    height: 48px;
  }
  .phone-number {
    position: absolute;
    left: 46px;
    top: 0;
    height: 48px;
    line-height: 48px;
    font-family: "Noto Serif", serif;
    font-size: 31px;
    color: var(--tan);
    white-space: nowrap;
  }
  .estimates {
    position: absolute;
    left: 549px;
    top: 284px;
    margin: 0;
    font-family: "Noto Serif", serif;
    font-size: 24px;
    line-height: 1;
    color: var(--tan);
    text-transform: uppercase;
    letter-spacing: 1px;
    white-space: nowrap;
  }
  .company-name {
    position: absolute;
    left: 57px;
    top: 402px;
    margin: 0;
    font-family: "Roboto Slab", serif;
    font-weight: 800;
    font-size: 52px;
    line-height: 60px;
    letter-spacing: 1px;
    color: var(--tan);
    text-transform: uppercase;
    white-space: nowrap;
  }
  .company-name .line-one { display: block; padding-left: 42px; }
  .company-name .line-two { display: block; }
  .company-name .suffix { font-size: 26px; letter-spacing: 2px; margin-left: 8px; }
  .services {
    position: absolute;
    left: 55px;
    top: 536px;
    margin: 0;
    padding: 0;
    list-style: none;
    font-family: "Noto Serif", serif;
    font-size: 30px;
    line-height: 36px;
    color: var(--tan);
    text-transform: uppercase;
    white-space: nowrap;
  }
  .services li {
    position: relative;
    padding-left: 31px;
  }
  .services li::before {
    content: "";
    position: absolute;
    left: 2px;
    top: 12px;
    width: 13px;
    height: 13px;
    border-radius: 50%;
    background: var(--stripe);
  }
  .bin-illustration {
    position: absolute;
    left: 831px;
    top: 390px;
    width: 321px;
    height: 238px;
    background: var(--bin-area);
    border-radius: 6px;
  }
  .insured-label {
    position: absolute;
    left: 842px;
    top: 592px;
    font-family: "Noto Serif", serif;
    font-size: 24px;
    line-height: 1;
    color: var(--ink);
  }
</style>
</head>
<body>
  <div class="card">
    <svg class="card-backdrop" width="1200" height="686" viewBox="0 0 1200 686" aria-hidden="true">
      <polygon class="corner-band" points="0,0 475,0 0,438" fill="var(--stripe)"/>
      <polygon class="corner-fill" points="0,0 452,0 0,415" fill="var(--tan)"/>
      <polygon class="corner-band" points="577,686 1200,5 1200,686" fill="var(--stripe)"/>
      <polygon class="corner-fill" points="600,686 1200,32 1200,686" fill="var(--tan)"/>
    </svg>

    <h1 class="owner-name">TODD DUNMORE</h1>

    <div class="phone-bar">
      <svg width="497" height="48" viewBox="0 0 497 48" aria-hidden="true">
        <rect x="0" y="0" width="353" height="48" fill="var(--ink)"/>
        <rect x="358" y="0" width="44" height="48" fill="var(--tan)"/>
        <rect x="407" y="0" width="90" height="48" fill="var(--ink)"/>
        <path d="M370 13 c2-2 5-2 6 0 l3 5 c1 2 0 3-1 4 l-2 2 c2 4 5 7 9 9 l2-2 c1-1 2-2 4-1 l5 3 c2 1 2 4 0 6 l-2 2 c-3 2-9 1-16-5 c-7-6-11-13-10-18 z" fill="var(--paper)"/>
      </svg>
      <span class="phone-number">555 268 0137</span>
    </div>

    <p class="estimates">Free Estimates</p>

    <h2 class="company-name">
      <span class="line-one">Dunmore Ag</span>
      <span class="line-two">Solutions,<span class="suffix">LLC</span></span>
    </h2>

    <ul class="services">
      <li>Sales</li>
      <li>Service</li>
      <li>Repair of Grain Bins</li>
    </ul>

    <div class="bin-illustration" role="img" aria-label="Line drawing of two grain bins with ladders"></div>
    <span class="insured-label">Insured</span>
  </div>
</body>
</html>
```